Business Cards

We were billed for this because the project timed out. Please give me another designed to open this back up. I was not happy with the last designs (that I was charged for).
we are also using the logo with Bringing Clear Water to Every Backyard
Also want to utilize Where Healthy Water is our Commitment.

Contact Information for Business Card

Marlowe Stone Group Inc

```html
<!DOCTYPE html>
<html lang="en">
<head>
<meta charset="utf-8">
<title>Marlowe Stone Group – Business Card</title>
<link rel="stylesheet" href="https://fonts.googleapis.com/css2?family=Orbitron:wght@500;700&family=Roboto:wght@400&display=swap">
<style>
  :root {
    --backdrop: #d1d2d4;
    --card-white: #ffffff;
    --brand-blue: #116bb3;
    --wave-light: #4aa3dc;
    --ink-dark: #3d3d3f;
    --ink-body: #4a4a4c;
    --divider: #555557;
    --water-deep: #3d8ea6;
    --water-light: #8cc3cf;
  }
  * { margin: 0; padding: 0; box-sizing: border-box; }
  html, body { width: 1200px; height: 1000px; overflow: hidden; }
  body { background: var(--backdrop); position: relative; font-family: "Roboto", Arial, sans-serif; }

  .card {
    position: absolute;
    left: 328px;
    width: 544px;
    height: 311px;
    overflow: hidden;
  }
  .card-front { top: 174px; background: var(--card-white); }
  .card-back { top: 515px; background: var(--brand-blue); }
  .card svg.card-art { position: absolute; inset: 0; width: 544px; height: 311px; }

  .brand-block {
    position: absolute;
    left: 38px;
    width: 214px;
    top: 160px;
    text-align: center;
  }
  .brand-name {
    font-family: "Orbitron", Arial, sans-serif;
    font-weight: 700;
    font-size: 11.5px;
    color: var(--ink-dark);
    white-space: nowrap;
    letter-spacing: 0.3px;
  }
  .brand-tagline {
    font-family: "Orbitron", Arial, sans-serif;
    font-weight: 500;
    font-size: 6.2px;
    color: var(--ink-dark);
    margin-top: 3px;
    white-space: nowrap;
    letter-spacing: 0.4px;
  }

  .divider {
    position: absolute;
    left: 267px;
    top: 82px;
    width: 1px;
    height: 146px;
    background: var(--divider);
  }

  .contact-block {
    position: absolute;
    left: 286px;
    top: 81px;
    color: var(--ink-body);
    font-size: 14px;
    line-height: 18px;
  }
  .person-name {
    font-family: "Orbitron", Arial, sans-serif;
    font-weight: 700;
    color: var(--brand-blue);
    font-size: 13.5px;
    line-height: 18px;
    letter-spacing: 0.8px;
  }
  .person-title { margin-bottom: 11px; }
  .address { margin-bottom: 7px; }
  .contact-line { display: flex; align-items: center; gap: 5px; height: 19px; }
  .contact-line svg { width: 13px; height: 13px; flex: none; fill: var(--brand-blue); }

  .back-brand {
    position: absolute;
    left: 0;
    width: 544px;
    top: 213px;
    text-align: center;
  }
  .back-brand .brand-name { color: var(--card-white); font-size: 21px; letter-spacing: 1px; }
  .back-brand .brand-tagline { color: var(--card-white); font-size: 10.5px; letter-spacing: 1.6px; margin-top: 5px; }
</style>
</head>
<body>

<section class="card card-front">
  <svg class="card-art" viewBox="0 0 544 311" aria-hidden="true">
    <path d="M0 288 C 110 268, 230 262, 340 270 C 430 277, 490 268, 544 238 L544 311 L0 311 Z" fill="var(--brand-blue)"/>
    <path d="M28 268 C 130 250, 260 248, 380 262 C 440 269, 490 270, 516 256 C 490 276, 440 280, 380 272 C 270 258, 150 256, 28 268 Z" fill="var(--wave-light)"/>
  </svg>

  <div class="brand-block">
    <div class="brand-name">MARLOWE STONE GROUP</div>
    <div class="brand-tagline">BRINGING CLEAR WATER TO EVERY BACKYARD</div>
  </div>

  <div class="divider"></div>

  <div class="contact-block">
    <div class="person-name">DANA R. WHITFIELD</div>
    <div class="person-title">Founder &amp; CEO</div>
    <div class="address">48 Harbor Lane, Suite 4<br>Linwood, MA 01940</div>
    <div class="contact-line">
      <svg viewBox="0 0 24 24"><path d="M6.6 10.8a15.1 15.1 0 0 0 6.6 6.6l2.2-2.2c.3-.3.7-.4 1-.2 1.1.4 2.3.6 3.6.6.6 0 1 .4 1 1V20c0 .6-.4 1-1 1C10.6 21 3 13.4 3 4c0-.6.4-1 1-1h3.5c.6 0 1 .4 1 1 0 1.3.2 2.5.6 3.6.1.3 0 .7-.2 1z"/></svg>
      <span>(555) 318-4720</span>
    </div>
    <div class="contact-line">
      <svg viewBox="0 0 24 24"><path d="M2 5h20v14H2z M4 7v.3l8 5.2 8-5.2V7z M4 9.6V17h16V9.6l-8 5.2z" fill-rule="evenodd"/></svg>
      <span>info@marlowestonegroup.com</span>
    </div>
    <div class="contact-line">
      <svg viewBox="0 0 24 24"><path d="M12 2a10 10 0 1 0 0 20 10 10 0 0 0 0-20zm6.9 6h-3a15 15 0 0 0-1.3-3.9A8 8 0 0 1 18.9 8zM12 4c.8 1.2 1.5 2.5 1.9 4h-3.8c.4-1.5 1.1-2.8 1.9-4zM4.3 14a8 8 0 0 1 0-4h3.4a16 16 0 0 0 0 4zm.8 2h3a15 15 0 0 0 1.3 3.9A8 8 0 0 1 5.1 16zm3-8h-3a8 8 0 0 1 4.3-3.9C8.9 5.2 8.4 6.6 8.1 8zM12 20c-.8-1.2-1.5-2.5-1.9-4h3.8c-.4 1.5-1.1 2.8-1.9 4zm2.3-6H9.7a14 14 0 0 1 0-4h4.6a14 14 0 0 1 0 4zm.3 5.9c.6-1.2 1-2.5 1.3-3.9h3a8 8 0 0 1-4.3 3.9zm1.7-5.9a16 16 0 0 0 0-4h3.4a8 8 0 0 1 0 4z"/></svg>
      <span>www.marlowestonegroup.com</span>
    </div>
  </div>
</section>

<section class="card card-back">
  <svg class="card-art" viewBox="0 0 544 311">
    <defs>
      <linearGradient id="waterTone" x1="0" y1="0" x2="1" y2="1">
        <stop offset="0" stop-color="var(--water-light)"/>
        <stop offset="1" stop-color="var(--water-deep)"/>
      </linearGradient>
    </defs>
    <path role="img" aria-label="Photo of feet splashing in clear pool water"
          d="M0 0 H544 V118 C 470 140, 380 142, 280 130 C 170 118, 80 118, 0 134 Z" fill="url(#waterTone)"/>
    <path d="M0 134 C 80 118, 170 118, 280 130 C 380 142, 470 140, 544 118" fill="none" stroke="var(--card-white)" stroke-width="3"/>
  </svg>

  <div class="back-brand">
    <div class="brand-name">MARLOWE STONE GROUP</div>
    <div class="brand-tagline">BRINGING CLEAR WATER TO EVERY BACKYARD</div>
  </div>
</section>

</body>
</html>
```